Real Estate Business Card

On the front side I want to have my info, my brokerage info.
On the back side I want have my complany’s logo, website and Facebook link. I will provide all this once I select a design.

I would like to see Black background and gold text, Dark Blue and gold text and White and blue text designs

Font styles to use
Sans Serif
Script

```html
<!DOCTYPE html>
<html lang="en">
<head>
<meta charset="utf-8">
<title>Ironpeak Realty – Business Card</title>
<link href="https://fonts.googleapis.com/css2?family=Montserrat:wght@800&family=Roboto:wght@400;500&display=swap" rel="stylesheet">
<style>
  :root {
    --backdrop: #2b2c2f;
    --card: #1c1d20;
    --gold: #e3bf55;
    --red: #e8363f;
    --slate: #8f97a6;
    --white: #f2f2f2;
    --rule: #b9bcc2;
  }
  * { margin: 0; padding: 0; box-sizing: border-box; }
  html, body { width: 1200px; height: 900px; overflow: hidden; }
  body {
    background: var(--backdrop);
    font-family: "Roboto", Arial, sans-serif;
    position: relative;
  }
  .card {
    position: absolute;
    left: 250px;
    width: 700px;
    height: 400px;
    background: var(--card);
    overflow: hidden;
  }
  .card--back { top: 40px; }
  .card--front { top: 460px; }

  .brand {
    display: flex;
    align-items: center;
    gap: 14px;
    position: absolute;
  }
  .brand__mark { background: var(--red); flex: none; }
  .brand__name {
    font-family: "Montserrat", Arial, sans-serif;
    font-weight: 800;
    color: var(--slate);
    letter-spacing: 0.5px;
    white-space: nowrap;
  }

  /* back side */
  .card--back .brand { left: 50px; top: 222px; }
  .card--back .brand__name { font-size: 30px; }
  .back-block {
    position: absolute;
    right: 40px;
    top: 60px;
    width: 300px;
    height: 300px;
    background: var(--red);
  }

  /* front side */
  .card--front .brand { right: 50px; top: 92px; }
  .card--front .brand__mark { width: 34px; height: 34px; }
  .card--front .brand__name { font-size: 30px; }

  .person { position: absolute; left: 70px; top: 150px; }
  .person__name {
    color: var(--gold);
    font-size: 28px;
    font-weight: 500;
    letter-spacing: 0.5px;
    line-height: 1;
  }
  .person__title {
    color: var(--red);
    font-size: 18px;
    font-weight: 500;
    margin-top: 4px;
  }
  .divider {
    position: absolute;
    left: 70px;
    right: 50px;
    top: 214px;
    height: 1px;
    background: var(--rule);
  }
  .contacts {
    position: absolute;
    left: 70px;
    top: 226px;
    list-style: none;
  }
  .contacts li {
    display: flex;
    align-items: center;
    gap: 12px;
    height: 27px;
    color: var(--white);
    font-size: 19px;
  }
  .contacts svg { width: 18px; height: 18px; fill: var(--gold); flex: none; }
  .address {
    position: absolute;
    right: 50px;
    top: 282px;
    text-align: right;
    color: var(--white);
    font-size: 19px;
    line-height: 1.3;
    font-style: normal;
  }
  .edge-stripe {
    position: absolute;
    left: 0; right: 0;
    bottom: 26px;
    height: 4px;
    background: var(--slate);
  }
  .edge-band {
    position: absolute;
    left: 0; right: 0; bottom: 0;
    height: 26px;
    background: linear-gradient(#ef4049, #c92a32);
  }
</style>
</head>
<body>

<section class="card card--back">
  <div class="brand">
    <span class="brand__name">IRONPEAK REALTY</span>
  </div>
  <div class="back-block"></div>
</section>

<section class="card card--front">
  <div class="brand">
    <span class="brand__mark"></span>
    <span class="brand__name">IRONPEAK REALTY</span>
  </div>

  <div class="person">
    <p class="person__name">DANIEL REYES</p>
    <p class="person__title">CEO/FOUNDER</p>
  </div>

  <div class="divider"></div>

  <ul class="contacts">
    <li>
      <svg viewBox="0 0 24 24" aria-hidden="true"><path d="M6.6 10.8a15 15 0 0 0 6.6 6.6l2.2-2.2c.3-.3.7-.4 1-.2 1.1.4 2.3.6 3.6.6.6 0 1 .4 1 1V20c0 .6-.4 1-1 1A17 17 0 0 1 3 4c0-.6.4-1 1-1h3.5c.6 0 1 .4 1 1 0 1.3.2 2.5.6 3.6.1.3 0 .7-.2 1z"/></svg>
      907 214 3360
    </li>
    <li>
      <svg viewBox="0 0 24 24" aria-hidden="true"><path d="M7 1h10a2 2 0 0 1 2 2v18a2 2 0 0 1-2 2H7a2 2 0 0 1-2-2V3a2 2 0 0 1 2-2zm0 3v14h10V4zm5 15.5a1 1 0 1 0 0 2 1 1 0 0 0 0-2z"/></svg>
      907 583 1472
    </li>
    <li>
      <svg viewBox="0 0 24 24" aria-hidden="true"><path d="M6 2h12v6H6zM3 9h18a2 2 0 0 1 2 2v7h-4v4H5v-4H1v-7a2 2 0 0 1 2-2zm4 8v3h10v-3z"/></svg>
      907 651 2089
    </li>
    <li>
      <svg viewBox="0 0 24 24" aria-hidden="true"><path d="M2 5h20v14H2zm2 2v.5l8 5.5 8-5.5V7zm0 2.9V17h16V9.9l-8 5.5z"/></svg>
      daniel@ironpeak.com
    </li>
  </ul>

  <address class="address">
    4120 Birchwood Drive<br>
    Juneau, Alaska 99801<br>
    www.ironpeak.com
  </address>

  <div class="edge-stripe"></div>
  <div class="edge-band"></div>
</section>

</body>
</html>
```